Futuristic Trade Show Booth Design for Quell Builders, Quell Designers, and Quell Corporate

We are seeking a cutting-edge and visually striking trade show booth design that showcases the synergy between our three brands: Quell Designers (architectural design), Quell Builders (construction services), and Quell Corporate (unified identity). The design must reflect our commitment to innovation, professionalism, and forward-thinking solutions for commercial design and construction.

The booth will include three panels and two podiums, with a modern and futuristic aesthetic. The focus is on creating a cohesive yet distinctive identity for each brand while highlighting their integration under Quell Corporate. Here’s what we envision:

Booth Specifications:
Backdrop Dimensions: Three panels of equal size.
Podiums: Two, one representing Quell Designers and the other Quell Builders.
Color Palette: Red (#D00E07), dark gray (#3B3838), light gray (#E0E0E0), and white (#FFFFFF).
Panel Breakdown:
1. Left Panel: Quell Designers (Architectural Focus)

Content:
Taglines like “Design Smarter”
Highlight Quell Designers’ architectural services : Commercial Architecture, Space Planning, Interior Design, Master Planning, 3D Renderings).
Visuals:
Include high-resolution 3D renderings of commercial spaces and modern blueprints.
Use a gradient background (dark gray to light gray) with overlays of translucent grids.
Icons representing architectural precision (e.g., drafting tools, rulers).
2. Center Panel: Quell Corporate (Unified Identity)
Content:
Central tagline: “Intergrated Design-Build Solution”
Unified messaging emphasizing Quell Corporate’s leadership in integrated design-build services.
Showcase how Quell Designers and Quell Builders collaborate seamlessly under Quell Corporate.
Visuals:
A split image showing half blueprints (design) and half construction (build).
Gradient background transitioning from red to gray for continuity.
Icons or a flowchart highlighting the steps: “Concept > Design > Build > Completion.”
3. Right Panel: Quell Builders (Construction Focus)

Content:
Taglines like “BUILD SMARTER
Highlight Quell Builders’ construction services (Construction Management, Design-Build, General Contracting, Pre-Construction).
Visuals:

Overlay dynamic construction elements like cranes, scaffolding, and hard hats.
LED accents or subtle motion graphics to emphasize innovation.
Podium Design:
Quell Designers Podium:
Gray-themed with the Quell Designers logo and tagline: “DESIGN SMARTER”
Quell Builders Podium:
Red-themed with the Quell Builders logo and tagline: “BUILD SMARTER.”
Design Requirements:
Must reflect a modern and futuristic aesthetic.
Use clean, bold typography (e.g., Yantramanav or similar).
Ensure cohesive branding across all panels while keeping individual identities for Quell Designers, Quell Builders, and Quell Corporate.
Balance professionalism with engaging visuals to attract visitors at the trade show.
Additional Notes:
The booth will serve as a centerpiece for showcasing Quell Corporate’s integrated approach to commercial design and construction. The design must communicate trust, innovation, and expertise while captivating the audience at first glance.

Quell Builders Website: www.quellbuilders.example
Quell Designers Website: www.quelldesigners.example
Quell Corporate: www.quellcorporate.example
Logo Quell Builders: https://files.example.net/share/a8Tq3LmZ0pWv7RcYx2NbK5sJd9HfGu4Ee
Logo Quell Designers: https://files.example.net/share/b3Kw8NpR1tYh6QdXz0MaL4cVf7JgSe2Uu
Logo Quell Corporate: https://files.example.net/share/c5Rn2HtB9wXk4PfVy1LdM8aZq6GjTo3Ii
The booth information and spec is on : https://www.standvelo.example/stand-ideas/linkup-10x10-stands/linkup-10x10-expo-stand-kit-c/

Target Market(s)

Commercial Property Developers, Corporate Real Estate Managers, Franchise Construction VP, Retail Franchise Owners,

Industry/Entity Type

Commercial Construction, Commercial Architecture

Font styles to use
Other font styles liked:
• Open to others but like Yantramanav, Poppins, Montserrat

Colors
EB3D1F
EC4F4E
F09395
F8D3D4
FCEDEE

Requirements
Must have
• Clear and prominent branding for Quell Designers, Quell Builders, and Quell Corporate on their respective panels. Consistent color scheme using red (#D00E07), dark gray (#3B3838), light gray (#E0E0E0), and white (#FFFFFF) to unify the design. A modern and futuristic aesthetic that reflects innovation, precision, and professionalism. Distinct yet cohesive representation of services offered by Quell Designers (architectural design), Quell Builders (construction), and Quell Corporate (integrated solutions).
Nice to have
• Subtle motion graphics or holographic overlays on panels to enhance the modern feel. A unified gradient background transitioning from red to gray to connect all panels visually. Visual flowcharts showing the step-by-step process of design-build services. Interactive design elements such as QR codes
Should not have
• Overly cluttered design that detracts from key messages or visuals. Fonts that are hard to read or do not match the modern and professional aesthetic. Excessive use of unrelated colors or mismatched visual styles. Misalignment or lack of clear separation between Quell Designers, Quell Builders, and Quell Corporate branding.

```html
<!DOCTYPE html>
<html lang="en">
<head>
<meta charset="utf-8">
<title>Quell Trade Show Booth – Panels and Podiums</title>
<link rel="stylesheet" href="https://fonts.googleapis.com/css2?family=Yantramanav:wght@900&family=Poppins:wght@400;500;600;700&display=swap">
<style>
:root{
  --red:#D00E07;
  --red-deep:#A9100C;
  --gray-dark:#3B3838;
  --gray-mid:#5E5B5B;
  --gray-light:#E0E0E0;
  --white:#FFFFFF;
  --ink:#222020;
  --lid:#1A1A1A;
}
*{box-sizing:border-box;margin:0;padding:0}
html,body{width:1200px;height:2249px;overflow:hidden}
body{
  background:linear-gradient(180deg,#F2F2F2 0%,var(--gray-light) 100%);
  font-family:"Poppins",sans-serif;color:var(--white);position:relative;
}
.backdrop{position:absolute;top:50px;left:24px;display:flex;gap:18px}
.panel{
  position:relative;width:372px;height:1020px;border-radius:64px 64px 0 0;overflow:hidden;
  display:flex;flex-direction:column;align-items:center;padding-top:78px;
}
.panel--designers{background:linear-gradient(180deg,#6A6868 0%,var(--gray-dark) 100%)}
.panel--corporate{background:linear-gradient(90deg,var(--gray-dark) 0%,#4A3A3A 40%,var(--red) 100%)}
.panel--builders{background:linear-gradient(180deg,var(--red) 0%,#B80D08 100%)}
.panel__photo{position:absolute;left:0;right:0;bottom:0;height:62%;opacity:.35;pointer-events:none}
.panel--designers .panel__photo{background:linear-gradient(180deg,transparent,#2A2828 70%)}
.panel--corporate .panel__photo{background:linear-gradient(90deg,#2E2C2C,transparent 55%,#8E0B07)}
.panel--builders .panel__photo{background:linear-gradient(200deg,transparent 10%,#7C0905 70%)}
.panel > *:not(.panel__photo){position:relative}

.brand{font-family:"Poppins",sans-serif;font-weight:600;font-size:26px;letter-spacing:5px;text-transform:uppercase;text-align:center;line-height:1.25;display:flex;align-items:center;gap:12px}
.brand__dot{width:14px;height:14px;background:var(--white)}

.headline{position:relative;margin-top:70px;text-align:center;font-family:"Yantramanav",sans-serif;font-weight:900;line-height:.9;text-transform:uppercase}
.headline__ghost{position:absolute;inset:0;color:transparent;-webkit-text-stroke:1px rgba(255,255,255,.35);transform:scale(1.28);transform-origin:center}
.headline__main{position:relative}
.headline--two{font-size:60px}
.headline--three{font-size:44px;line-height:.98}

.subhead{margin-top:40px;font-weight:600;font-size:21px;text-align:center;line-height:1.25}

.services{margin-top:34px;display:grid;grid-template-columns:1fr 1fr;gap:32px 36px;width:300px}
.service{display:flex;flex-direction:column;align-items:center;text-align:center;font-size:17px;line-height:1.2}
.service--center{grid-column:1 / span 2}
.service__badge{width:76px;height:76px;border-radius:50%;background:var(--red);border:2px solid rgba(255,255,255,.35);display:flex;align-items:center;justify-content:center;margin-bottom:12px}
.panel--builders .service__badge{width:88px;height:88px;background:var(--gray-dark)}
.panel--builders .services{gap:48px 30px;margin-top:48px}
.panel--builders .service{font-size:18px}
.service__badge svg{width:42px;height:42px}

.url{margin-top:auto;margin-bottom:40px;background:var(--white);color:var(--ink);font-weight:500;font-size:14px;letter-spacing:1px;padding:6px 18px;border-radius:20px}

.pill{margin-top:30px;background:rgba(255,255,255,.25);font-weight:600;font-size:15px;padding:4px 16px;border-radius:14px}
.flow{margin-top:16px;display:flex;gap:10px;align-items:center}
.step{display:flex;flex-direction:column;align-items:center;font-size:11px;font-weight:600;gap:4px}
.step__num{font-size:13px;color:rgba(255,255,255,.55)}
.step__circle{width:66px;height:66px;border-radius:50%;background:var(--white);border:5px solid rgba(255,255,255,.4);display:flex;align-items:center;justify-content:center}
.step__circle svg{width:34px;height:34px}
.industries-title{margin-top:34px;font-weight:600;font-size:16px}
.industries{margin-top:18px;display:grid;grid-template-columns:repeat(3,1fr);gap:22px 10px;width:340px}
.industry{display:flex;align-items:center;gap:6px;font-size:10.5px;font-weight:600;line-height:1.15}
.industry svg{width:22px;height:22px;flex:none}

/* podiums */
.podiums{position:absolute;top:1170px;left:60px;display:flex;gap:120px}
.podium{width:480px}
.podium__lid{height:46px;background:var(--lid);border-radius:10px 10px 4px 4px;margin:0 -14px}
.podium__front{height:560px;display:flex;flex-direction:column;align-items:center;padding-top:90px}
.podium--designers .podium__front{background:linear-gradient(180deg,#6A6868,var(--gray-dark))}
.podium--builders .podium__front{background:linear-gradient(180deg,var(--red),#B80D08)}
.podium .headline{margin-top:80px}
.podium .headline--two{font-size:70px}
.podium__url{margin-top:auto;margin-bottom:60px;font-size:15px;letter-spacing:1px}
</style>
</head>
<body>
<main class="booth">
  <section class="backdrop">
    <!-- Designers -->
    <article class="panel panel--designers">
      <div class="panel__photo" role="img" aria-label="Faint 3D rendering of a modern commercial building with blueprint grid overlay"></div>
      <div class="brand"><span class="brand__dot"></span>Quell<br>Designers</div>
      <h2 class="headline headline--two"><span class="headline__ghost" aria-hidden="true">Design<br>Smarter</span><span class="headline__main">Design<br>Smarter</span></h2>
      <p class="subhead">Architectural Services</p>
      <ul class="services">
        <li class="service"><span class="service__badge"><svg viewBox="0 0 40 40" fill="none" stroke="#fff" stroke-width="2"><rect x="6" y="8" width="24" height="26"/><path d="M10 28 28 10M30 6l4 4"/></svg></span>Commercial Architecture</li>
        <li class="service"><span class="service__badge"><svg viewBox="0 0 40 40" fill="none" stroke="#fff" stroke-width="2"><rect x="8" y="8" width="24" height="24"/><path d="M14 8v24M20 8v24M26 8v24M8 14h24M8 20h24M8 26h24"/></svg></span>Space Planning</li>
        <li class="service"><span class="service__badge"><svg viewBox="0 0 40 40" fill="none" stroke="#fff" stroke-width="2"><path d="M6 32h28M9 32V14h22v18M9 20h22M15 20v12M21 20v12M27 20v12M12 14l8-6 8 6"/></svg></span>Master Planning</li>
        <li class="service"><span class="service__badge"><svg viewBox="0 0 40 40" fill="none" stroke="#fff" stroke-width="2"><rect x="8" y="6" width="24" height="28"/><path d="M8 18h12M20 6v20M20 26h12"/></svg></span>Interior Design</li>
        <li class="service service--center"><span class="service__badge"><svg viewBox="0 0 40 40" fill="none" stroke="#fff" stroke-width="2"><path d="M20 6 33 13v14L20 34 7 27V13z M7 13l13 7 13-7M20 20v14"/></svg></span>3D Renderings</li>
      </ul>
      <span class="url">www.quelldesigners.example</span>
    </article>

    <!-- Corporate -->
    <article class="panel panel--corporate">
      <div class="panel__photo" role="img" aria-label="Split image of architectural blueprints and a building under construction"></div>
      <div class="brand"><span class="brand__dot"></span>Quell<br>Corporate</div>
      <h1 class="headline headline--three"><span class="headline__ghost" aria-hidden="true">Intergrated<br>Design-Build<br>Solution</span><span class="headline__main">Intergrated<br>Design-Build<br>Solution</span></h1>
      <p class="subhead">Expertise Across Diverse<br>Commercial Sector</p>
      <span class="pill">How We Work?</span>
      <ol class="flow">
        <li class="step"><span class="step__num">01</span><span class="step__circle"><svg viewBox="0 0 40 40" fill="none" stroke="#3B3838" stroke-width="2.5"><rect x="8" y="10" width="24" height="22"/><path d="M8 20h24M20 10v22" stroke="#D00E07"/></svg></span>Concept</li>
        <li class="step">Design<span class="step__circle"><svg viewBox="0 0 40 40" fill="none" stroke="#3B3838" stroke-width="2.5"><rect x="8" y="8" width="24" height="24"/><path d="M12 28 28 12" stroke="#D00E07"/></svg></span><span class="step__num">02</span></li>
        <li class="step"><span class="step__num">03</span><span class="step__circle"><svg viewBox="0 0 40 40" fill="none" stroke="#3B3838" stroke-width="2.5"><path d="M10 34V8h4v26M14 10h18M28 10v8" /><rect x="18" y="22" width="14" height="12" stroke="#D00E07"/></svg></span>Build</li>
        <li class="step">Completion<span class="step__circle"><svg viewBox="0 0 40 40" fill="none" stroke="#3B3838" stroke-width="2.5"><path d="M6 20 20 8l14 12M10 17v16h20V17"/><rect x="17" y="23" width="6" height="10" fill="#D00E07" stroke="none"/></svg></span><span class="step__num">04</span></li>
      </ol>
      <p class="industries-title">Tailored Solutions for Every Industry</p>
      <ul class="industries">
        <li class="industry"><svg viewBox="0 0 24 24" fill="none" stroke="#fff" stroke-width="1.5"><rect x="4" y="3" width="16" height="18"/><path d="M8 7h2M14 7h2M8 11h2M14 11h2M8 15h2M14 15h2"/></svg>Multifamily</li>
        <li class="industry"><svg viewBox="0 0 24 24" fill="none" stroke="#fff" stroke-width="1.5"><rect x="4" y="5" width="16" height="16"/><path d="M4 9h16M10 21v-5h4v5"/></svg>Hospitality</li>
        <li class="industry"><svg viewBox="0 0 24 24" fill="none" stroke="#fff" stroke-width="1.5"><path d="M3 10 12 4l9 6v11H3zM9 21v-6h6v6"/></svg>Restaurants</li>
        <li class="industry"><svg viewBox="0 0 24 24" fill="none" stroke="#fff" stroke-width="1.5"><path d="M3 9h18v12H3zM3 9l2-5h14l2 5M9 21v-6h6v6"/></svg>Retail Centers</li>
        <li class="industry"><svg viewBox="0 0 24 24" fill="none" stroke="#fff" stroke-width="1.5"><rect x="6" y="3" width="12" height="18"/><path d="M9 7h6M9 11h6M9 15h6"/></svg>Corporate</li>
        <li class="industry"><svg viewBox="0 0 24 24" fill="none" stroke="#fff" stroke-width="1.5"><rect x="4" y="6" width="16" height="15"/><path d="M12 9v6M9 12h6"/></svg>Healthcare Facilities</li>
        <li class="industry"><svg viewBox="0 0 24 24" fill="none" stroke="#fff" stroke-width="1.5"><path d="M3 21V10l9-5 9 5v11zM7 21v-6h10v6"/></svg>Industrial / Warehouse</li>
        <li class="industry"><svg viewBox="0 0 24 24" fill="none" stroke="#fff" stroke-width="1.5"><path d="M12 2v5M10 4h4M4 21l8-12 8 12zM10 21v-4h4v4"/></svg>Religious Institutions</li>
        <li class="industry"><svg viewBox="0 0 24 24" fill="none" stroke="#fff" stroke-width="1.5"><path d="M3 21V8h7v13M10 21V3h11v18M13 7h5M13 11h5M13 15h5"/></svg>Mixed-Use Developments</li>
      </ul>
      <span class="url">www.quellcorporate.example</span>
    </article>

    <!-- Builders -->
    <article class="panel panel--builders">
      <div class="panel__photo" role="img" aria-label="Faint photo of a construction site with cranes and scaffolding"></div>
      <div class="brand"><span class="brand__dot"></span>Quell<br>Builders</div>
      <h2 class="headline headline--two"><span class="headline__ghost" aria-hidden="true">Build<br>Smarter</span><span class="headline__main">Build<br>Smarter</span></h2>
      <p class="subhead">Construction Services</p>
      <ul class="services">
        <li class="service"><span class="service__badge"><svg viewBox="0 0 40 40" fill="none" stroke="#fff" stroke-width="2"><path d="M8 22a12 12 0 0 1 24 0zM6 22h28M20 10V6"/><rect x="10" y="26" width="20" height="8"/></svg></span>Construction Management</li>
        <li class="service"><span class="service__badge"><svg viewBox="0 0 40 40" fill="none" stroke="#fff" stroke-width="2"><rect x="10" y="12" width="20" height="22"/><path d="M14 17h4M22 17h4M14 23h4M22 23h4M10 8h24M30 8v6"/></svg></span>Design-Build</li>
        <li class="service"><span class="service__badge"><svg viewBox="0 0 40 40" fill="none" stroke="#fff" stroke-width="2"><circle cx="14" cy="14" r="6"/><path d="M8 34v-6a8 8 0 0 1 16 0v6M24 10h10M29 10v16"/></svg></span>General Contracting</li>
        <li class="service"><span class="service__badge"><svg viewBox="0 0 40 40" fill="none" stroke="#fff" stroke-width="2"><path d="M6 20 20 8l14 12M10 17v17h20V17M12 32 28 18"/></svg></span>Pre-Construction</li>
      </ul>
      <span class="url">www.quellbuilders.example</span>
    </article>
  </section>

  <section class="podiums">
    <article class="podium podium--designers">
      <div class="podium__lid"></div>
      <div class="podium__front">
        <div class="brand"><span class="brand__dot"></span>Quell Designers</div>
        <h2 class="headline headline--two"><span class="headline__main">Design<br>Smarter</span></h2>
        <span class="podium__url">www.quelldesigners.example</span>
      </div>
    </article>
    <article class="podium podium--builders">
      <div class="podium__lid"></div>
      <div class="podium__front">
        <div class="brand"><span class="brand__dot"></span>Quell Builders</div>
        <h2 class="headline headline--two"><span class="headline__main">Build<br>Smarter</span></h2>
        <span class="podium__url">www.quellbuilders.example</span>
      </div>
    </article>
  </section>
</main>
</body>
</html>
```